Redesign the *Settings* screen for the PelikoZ app.

PelikoZ app is in production, but we need to refresh and redesign the settings screen to be cleaner, easier, more intuitive, and more professional looking.

Project Deadline Extended
Reason: Several designers have requested more time. This will also give time to provide feedback on existing designs.

Requirements
Must have
• Black background, so that the screen is consistent with the rest of the app.

```html
<!DOCTYPE html>
<html lang="en">
<head>
<meta charset="utf-8">
<title>PelikoZ – Settings</title>
<link href="https://fonts.googleapis.com/css2?family=Roboto:wght@400;500&display=swap" rel="stylesheet">
<style>
:root{
  --page:#ffffff;
  --status:#3a4356;
  --surface:#2e384c;
  --header:#222a3a;
  --divider:#263043;
  --text:#ffffff;
  --accent:#5dfc6b;
  --accent-dark:#3f8f48;
  --toggle-off:#7784a3;
  --toggle-off-track:#4a556e;
  --icon-muted:#4b5670;
  --danger:#e9531f;
}
*{box-sizing:border-box;margin:0;padding:0}
html,body{width:1200px;height:910px;overflow:hidden;background:var(--page)}
body{font-family:'Roboto',sans-serif;color:var(--text);position:relative}
.screen{position:absolute;left:412px;top:4px;width:375px;height:901px;background:var(--surface);display:flex;flex-direction:column}
.status-bar{height:22px;background:var(--status);display:flex;align-items:center;justify-content:space-between;padding:0 8px 0 6px;font-size:11.5px}
.status-bar .carrier,.status-bar .battery{display:flex;align-items:center;gap:4px}
.battery-icon{width:22px;height:10px;border:1px solid #fff;border-radius:2px;position:relative}
.battery-icon::before{content:"";position:absolute;left:1px;top:1px;width:8px;height:6px;background:#fff}
.title-bar{height:61px;display:flex;align-items:center;justify-content:center;font-size:18px}
.section-header{height:47px;background:var(--header);display:flex;align-items:center;justify-content:space-between;padding:0 22px 0 20px;font-size:14.5px;font-weight:500}
.info-icon{width:14px;height:14px;border-radius:50%;background:#a9aeb9;color:var(--header);font-size:10px;font-style:italic;font-weight:500;display:flex;align-items:center;justify-content:center;font-family:Georgia,serif}
.segmented{height:46px;display:flex}
.segment{flex:1;display:flex;align-items:center;justify-content:center;font-size:16px}
.segment.is-active{background:var(--accent);color:#1f3a24}
.row{height:54px;display:flex;align-items:center;padding:0 20px;border-bottom:1px solid var(--divider);font-size:16px}
.row .label{flex:1}
.row .lead{width:56px;display:flex;align-items:center}
.checkbox{width:19px;height:19px;border:2px solid #fff}
.checkbox.is-checked{background:var(--accent);border-color:var(--accent);display:flex;align-items:center;justify-content:center}
.toggle{width:40px;height:24px;position:relative}
.toggle::before{content:"";position:absolute;left:0;top:7px;width:40px;height:11px;border-radius:6px;background:var(--toggle-off-track)}
.toggle::after{content:"";position:absolute;left:0;top:1px;width:22px;height:22px;border-radius:50%;background:var(--toggle-off)}
.toggle.is-on::before{background:var(--accent-dark)}
.toggle.is-on::after{left:18px;background:var(--accent)}
.gap{height:6px;background:var(--header)}
.gap.wide{height:8px}
.row.no-border{border-bottom:none}
.version{height:77px;padding:17px 20px 0;font-size:16px;line-height:21px;border-bottom:1px solid var(--divider)}
.tab-bar{flex:1;display:flex;align-items:center;justify-content:space-between;padding:0 20px 0 14px}
</style>
</head>
<body>
<main class="screen">
  <div class="status-bar">
    <span class="carrier">●●●○○ Nimbo
      <svg width="12" height="9" viewBox="0 0 12 9"><path d="M1 3a7 7 0 0 1 10 0M3 5a4 4 0 0 1 6 0" stroke="#fff" stroke-width="1.3" fill="none"/><circle cx="6" cy="7.5" r="1.1" fill="#fff"/></svg>
    </span>
    <span class="time">9:41 AM</span>
    <span class="battery">
      <svg width="8" height="11" viewBox="0 0 8 11"><path d="M1 3l6 5-3 2.5V.5L7 3 1 8" stroke="#fff" fill="none"/></svg>
      42% <span class="battery-icon"></span>
    </span>
  </div>

  <header class="title-bar">Settings</header>

  <div class="section-header">Device Mount Position <span class="info-icon">i</span></div>
  <div class="segmented">
    <div class="segment is-active">Forwards</div>
    <div class="segment">Backwards</div>
  </div>

  <div class="section-header">Device Mount Location <span class="info-icon">i</span></div>
  <div class="row"><span class="lead"><span class="checkbox is-checked"><svg width="13" height="10" viewBox="0 0 13 10"><path d="M1 5l4 4 7-8" stroke="#fff" stroke-width="1.6" fill="none"/></svg></span></span><span class="label">Bottom</span></div>
  <div class="row"><span class="lead"><span class="checkbox"></span></span><span class="label">Top</span></div>
  <div class="row"><span class="lead"><span class="checkbox"></span></span><span class="label">Left</span></div>
  <div class="row no-border"><span class="lead"><span class="checkbox"></span></span><span class="label">Right</span></div>

  <div class="section-header">Bullseye Mode <span class="info-icon">i</span></div>
  <div class="row no-border"><span class="label">ON</span><span class="toggle is-on"></span></div>
  <div class="gap"></div>

  <div class="row">
    <span class="lead"><svg width="34" height="34" viewBox="0 0 34 34"><circle cx="17" cy="17" r="16" stroke="var(--icon-muted)" fill="none" stroke-width="1.5"/><path d="M10 17a7 7 0 0 1 12-5M24 17a7 7 0 0 1-12 5" stroke="var(--icon-muted)" stroke-width="1.5" fill="none"/><path d="M22 8v4h-4M12 26v-4h4" stroke="var(--icon-muted)" stroke-width="1.5" fill="none"/></svg></span>
    <span class="label">Sync</span><span class="toggle"></span>
  </div>
  <div class="row">
    <span class="lead"><svg width="34" height="30" viewBox="0 0 34 30"><path d="M12 9l12 11-6 6V3l6 6-12 11" stroke="#fff" stroke-width="1.2" fill="none"/></svg></span>
    <span class="label">Bluetooth</span><span class="toggle is-on"></span>
  </div>
  <div class="row no-border">
    <span class="lead"><svg width="34" height="30" viewBox="0 0 34 30"><path d="M15 2v27" stroke="var(--icon-muted)" stroke-width="1.5"/><path d="M15 2l18 8-18 8z" fill="var(--icon-muted)"/></svg></span>
    <span class="label">Report</span><span class="toggle"></span>
  </div>
  <div class="gap wide"></div>

  <div class="row no-border">
    <span class="label">Logout</span>
    <svg width="28" height="28" viewBox="0 0 28 28"><path d="M8 7a10 10 0 1 0 12 0" stroke="var(--danger)" stroke-width="1.8" fill="none"/><path d="M14 2v11" stroke="var(--danger)" stroke-width="1.8"/></svg>
  </div>
  <div class="gap"></div>

  <div class="version">App Version:<br>2.3.9.05</div>

  <nav class="tab-bar">
    <svg width="26" height="26" viewBox="0 0 26 26"><circle cx="13" cy="13" r="12" stroke="var(--icon-muted)" fill="none" stroke-width="1.5"/><circle cx="13" cy="13" r="8" stroke="var(--icon-muted)" fill="none" stroke-width="1.5"/><circle cx="13" cy="13" r="4" stroke="var(--icon-muted)" fill="none" stroke-width="1.5"/></svg>
    <svg width="24" height="24" viewBox="0 0 24 24"><rect x="1" y="3" width="22" height="20" stroke="var(--icon-muted)" fill="none" stroke-width="1.5"/><path d="M1 8h22M6 1v4M18 1v4M5 12h14M5 15h14M5 18h14" stroke="var(--icon-muted)" stroke-width="1.2"/></svg>
    <svg width="34" height="28" viewBox="0 0 34 28"><path d="M17 3L2 10l15 7 15-7z" stroke="var(--icon-muted)" fill="none" stroke-width="1.5"/><path d="M8 13v7c4 4 14 4 18 0v-7M29 11v14" stroke="var(--icon-muted)" fill="none" stroke-width="1.5"/></svg>
    <svg width="28" height="28" viewBox="0 0 28 28"><path d="M12 1h4l1 4 3 1.5 3.5-2 3 3-2 3.5L26 12l1 0v4l-4 1-1.5 3 2 3.5-3 3-3.5-2L16 26l0 1h-4l-1-4-3-1.5-3.5 2-3-3 2-3.5L2 16H1v-4l4-1 1.5-3-2-3.5 3-3 3.5 2L12 5z" stroke="#fff" fill="none" stroke-width="1.3"/><circle cx="14" cy="14" r="5" stroke="#fff" fill="none" stroke-width="1.3"/><circle cx="14" cy="14" r="2" stroke="#fff" fill="none" stroke-width="1.3"/></svg>
  </nav>
</main>
</body>
</html>
```